Re design current site.

Redesign of the current site. Like current design But I don't own it so I need a custom design similar to the current one. Want the model pictures to be shown off as they currently do on the home page I want to show off contact info make it very noticeable and readable.
Target Market(s)
Males age 30-60
Number of Pages Required
1 page
Requirements
Must have
- Must show off model pictures on the page. Must show contact info easy to read easy to find.

```html
<!DOCTYPE html>
<html lang="en">
<head>
<meta charset="utf-8">
<title>Vela Models</title>
<link href="https://fonts.googleapis.com/css2?family=Exo+2:wght@300;400;500&family=Lato:wght@400;700&display=swap" rel="stylesheet">
<style>
:root{
  --black:#000;
  --panel:#1a1a1a;
  --dark:#111;
  --red:#e3242b;
  --white:#fff;
  --grey:#bdbdbd;
  --line:#555;
}
*{box-sizing:border-box;margin:0;padding:0}
html,body{width:1200px;height:2590px;overflow:hidden;background:var(--black)}
body{position:relative;font-family:'Lato',sans-serif;color:var(--white)}
.abs{position:absolute}
.head{font-family:'Exo 2',sans-serif;font-weight:400;text-transform:uppercase;letter-spacing:.5px}
.red{color:var(--red)}

.topbar{left:0;top:0;width:1200px;height:48px;border-bottom:1px solid #222}
.topbar .mail{left:69px;top:13px;font-size:14px;display:flex;align-items:center;gap:10px}
.mail-icon{width:22px;height:18px;border:1px solid var(--red);display:flex;align-items:center;justify-content:center}
.social{right:70px;top:12px;display:flex;gap:8px}
.social span{width:22px;height:22px;background:#2b5aa8;display:block}
.social span:nth-child(3){background:#2a9fd8}
.social span:nth-child(4){background:#d24b36}

.brand{left:70px;top:74px;display:flex;align-items:center;gap:10px;font-family:'Exo 2',sans-serif;font-size:30px;font-weight:400;letter-spacing:1px}
.brand i{width:26px;height:40px;background:var(--white);display:block}
.nav{left:459px;top:90px;display:flex;gap:28px;font-family:'Exo 2',sans-serif;font-size:13px;text-transform:uppercase;white-space:nowrap}
.nav .on{color:var(--red)}
.phone{right:66px;top:72px;text-align:right;white-space:nowrap}
.phone b{display:block;font-family:'Exo 2',sans-serif;font-weight:400;font-size:22px;line-height:26px;color:var(--red)}
.phone small{font-size:13px}

.hero{left:71px;top:150px;width:1058px;height:411px;background:linear-gradient(120deg,#e8e4e2 0%,#a78876 35%,#3b2c28 70%,#1a1a1c 100%)}
.caption{left:744px;top:397px;width:375px;height:130px;background:rgba(0,0,0,.65);text-align:center;padding-top:16px;font-family:'Exo 2',sans-serif;font-size:40px;line-height:48px;white-space:nowrap}
.caption .head{font-size:40px}
.arrow{top:342px}

.sec-title{width:1200px;left:0;text-align:center;font-size:28px}
.rule{left:578px;width:44px;height:2px;background:var(--red)}

.card{top:699px;width:223px;height:296px}
.c1{left:71px;background:linear-gradient(160deg,#cfd6d3,#b78f76 60%,#6f5a50)}
.c2{left:349px;background:linear-gradient(170deg,#5a7a3a,#c9a58e 55%,#3f5a2a)}
.c3{left:627px;background:linear-gradient(170deg,#3a3030,#b08670 50%,#4a3b38)}
.c4{left:907px;background:linear-gradient(170deg,#444,#d9a18a 35%,#d3343a 75%,#3a2c28)}
.bio{left:71px;top:699px;width:124px;height:296px;background:rgba(227,36,43,.92);padding:38px 0 0 16px}
.bio h3{font-family:'Exo 2',sans-serif;font-weight:400;font-size:20px;margin-bottom:28px}
.bio dl{font-size:12px;line-height:19px;display:grid;grid-template-columns:50px 1fr}
.bio .btn{position:absolute;left:10px;top:170px;width:98px;height:32px;background:#111;font-size:13px;text-align:center;line-height:32px;font-family:'Exo 2',sans-serif;text-transform:uppercase}

.btn-red{background:var(--red);text-align:center;font-family:'Exo 2',sans-serif;text-transform:uppercase;font-size:14px;white-space:nowrap}

.about{left:0;top:1131px;width:1200px;height:556px;background:var(--panel)}
.about-photo{left:0;top:1131px;width:640px;height:556px;background:linear-gradient(90deg,#2a2224,#7a5a50 45%,#3a3030 80%,var(--panel))}
.about-text{left:653px;top:1256px;width:480px;font-size:14.5px;line-height:22.5px;color:#e6e6e6}
.about-text p{margin-bottom:13px}

.banner{left:202px;top:1730px;width:796px;height:76px;background:#2a2a2a;padding:6px}
.banner-in{width:100%;height:100%;background:linear-gradient(90deg,#7a2a2c,#d0676a 45%,#f07a52 80%,#c85a3a);position:relative;padding:6px 0 0 80px}
.banner-in h4{font-family:'Exo 2',sans-serif;font-weight:300;font-size:34px;color:rgba(255,255,255,.55);line-height:36px}
.banner-in small{display:inline-block;background:#b83a3c;color:#fbd;font-size:10px;padding:2px 8px}

.news{left:0;top:1851px;width:1200px;height:339px;background:linear-gradient(90deg,#2a2426,#4a3e3a 30%,#1c1a1c 60%,#2c2628)}
.news-text{left:180px;top:1992px;width:840px;text-align:center;font-size:14.5px;line-height:22px}
.email-in{left:395px;top:2083px;width:273px;height:41px;background:var(--white);color:#333;font-size:13px;padding:12px 22px}
.subscribe{left:668px;top:2083px;width:120px;height:41px;line-height:41px}

.contact-info{left:80px;font-size:12px;line-height:17px}
.contact-info b{display:block;text-transform:uppercase;font-weight:700}
.ico{position:absolute;left:-2px}
.contact-info div{padding-left:20px;position:relative}
.field{left:515px;width:290px;height:35px;border:1px solid var(--line);font-size:11px;color:#aaa;padding:10px 16px}
.message{left:841px;top:2316px;width:288px;height:130px;border:1px solid var(--line);font-size:11px;color:#aaa;padding:12px 16px}
.submit{left:841px;top:2461px;width:288px;height:35px;line-height:35px}

.footer{left:0;top:2547px;width:1200px;height:43px;border-top:1px solid #222;background:#0a0a0a}
.footer p{position:absolute;left:72px;top:14px;font-size:12px}
.cards{position:absolute;right:70px;top:10px;display:flex;gap:6px}
.cards span{width:32px;height:22px;background:#eee;border-radius:2px;display:block}
</style>
</head>
<body>

<header>
  <div class="abs topbar">
    <div class="abs mail"><span class="mail-icon"><svg width="12" height="9" viewBox="0 0 12 9"><rect x="0.5" y="0.5" width="11" height="8" fill="#fff"/><path d="M0.5 0.5 L6 5 L11.5 0.5" stroke="#000" fill="none"/></svg></span>Hello@VelaModels.com</div>
    <div class="abs social" aria-label="Social links"><span></span><span></span><span></span><span></span></div>
  </div>
  <div class="abs brand"><i></i>VELA MODELS</div>
  <nav class="abs nav"><span class="on">Home</span><span>About</span><span>Bookings</span><span>Rates</span><span>Models</span><span>Employment</span><span>Links</span></nav>
  <div class="abs phone"><b>(555) 201 4870</b><small>24/7 free calls</small></div>
</header>

<section>
  <div class="abs hero" role="img" aria-label="Slideshow photo of a featured model reclining on a sofa"></div>
  <div class="abs caption"><span class="head">Vela <span class="red">Models</span></span><br>Concierge Service</div>
  <svg class="abs arrow" style="left:24px" width="22" height="20" viewBox="0 0 22 20"><path d="M10 2 L2 10 L10 18 M20 2 L12 10 L20 18" stroke="#fff" stroke-width="2.5" fill="none"/></svg>
  <svg class="abs arrow" style="left:1156px" width="22" height="20" viewBox="0 0 22 20"><path d="M2 2 L10 10 L2 18 M12 2 L20 10 L12 18" stroke="#e3242b" stroke-width="2.5" fill="none"/></svg>
</section>

<section>
  <h2 class="abs sec-title head" style="top:598px"><span class="red">Our</span> Models</h2>
  <div class="abs rule" style="top:652px"></div>
  <div class="abs card c1" role="img" aria-label="Model photo"></div>
  <div class="abs bio">
    <h3>Sienna</h3>
    <dl><dt>Age:</dt><dd>23</dd><dt>Height:</dt><dd>5'0</dd><dt>Weight:</dt><dd>110</dd></dl>
    <span class="btn">View Bio</span>
  </div>
  <div class="abs card c2" role="img" aria-label="Model photo in a garden"></div>
  <div class="abs card c3" role="img" aria-label="Model photo"></div>
  <div class="abs card c4" role="img" aria-label="Model photo"></div>
  <div class="abs btn-red" style="left:518px;top:1038px;width:164px;height:38px;line-height:38px">View All Model</div>
</section>

<section>
  <div class="abs about"></div>
  <div class="abs about-photo" role="img" aria-label="Model seated on a chair holding a rose"></div>
  <h2 class="abs head" style="left:653px;top:1177px;font-size:27px"><span class="red">About</span> Vela <span class="red">Models</span></h2>
  <div class="abs" style="left:653px;top:1228px;width:42px;height:2px;background:var(--red)"></div>
  <div class="abs about-text">
    <p>VelaModels Concierge Service allows clients to request VelaModels to search for models in the location you plan on traveling to. We will search and find attractive models for the dates requested. We also verify they are interested in the service you expect/request and that the pictures we have are recent and real.</p>
    <p>Are you looking for the best Miami companion services providing incall and outcall serving the Miami, Fort Lauderdale, West Palm Beach &amp; other major city's? If so, then you have come to the right place! With the most beautiful, hot, sexy and sizzling companions in the Miami, Fort Lauderdale &amp; West Palm Beach areas. Click Here to See Our Models!</p>
    <p>we, at VelaModels, can accommodate your dreams &amp; demands for any and all kinds of engagements. Our main goal is to offer you a fully satisfying, warm, and pleasurable encounter that you will never forget!</p>
  </div>
  <div class="abs btn-red" style="left:653px;top:1596px;width:124px;height:38px;line-height:38px">Read More</div>
</section>

<aside class="abs banner">
  <div class="banner-in" role="img" aria-label="Recruitment banner with a model photo">
    <h4>Wanna be a Model?</h4>
    <small>Call us now to know how!</small>
  </div>
</aside>

<section>
  <div class="abs news" role="img" aria-label="Soft background photo of a model"></div>
  <h2 class="abs sec-title head" style="top:1905px"><span class="red">Join My</span> Newsletter</h2>
  <div class="abs rule" style="top:1958px"></div>
  <p class="abs news-text">Lorem ipsum dolor sit amet, consectetuer adipiscing elit, sed diam nonummy nibh euismod tincidunt ut laoreet dolore magna aliquam erat volutpat. Ut wisi enim ad minim veniam.</p>
  <svg class="abs" style="left:330px;top:2030px" width="70" height="70" viewBox="0 0 70 70"><circle cx="35" cy="35" r="33" stroke="#e3242b" stroke-opacity=".35" fill="none"/><path d="M4 28 L64 8 L36 54 L30 34 Z" fill="#e3242b"/></svg>
  <div class="abs email-in">Enter your email address</div>
  <div class="abs btn-red subscribe">Subscribe</div>
</section>

<section>
  <h2 class="abs sec-title head" style="top:2224px"><span class="red">Contact</span> Us</h2>
  <div class="abs rule" style="top:2276px"></div>
  <div class="abs contact-info" style="top:2316px"><div><svg class="ico" width="10" height="14" viewBox="0 0 10 14"><path d="M5 0 A5 5 0 0 1 10 5 C10 9 5 14 5 14 C5 14 0 9 0 5 A5 5 0 0 1 5 0Z" fill="#e3242b"/><circle cx="5" cy="5" r="2" fill="#000"/></svg><b>Address:</b>123 Lorem ipsum dolor sit amet, consectetuer<br>adipiscing elit, sed diam nonummy</div></div>
  <div class="abs contact-info" style="top:2396px"><div><svg class="ico" width="12" height="12" viewBox="0 0 12 12"><path d="M2 0 L4.5 0 L5 3 L3.5 4.5 C4.5 6.5 5.5 7.5 7.5 8.5 L9 7 L12 7.5 L12 10 C12 11 11 12 10 12 C4.5 12 0 7.5 0 2 C0 1 1 0 2 0Z" fill="#e3242b"/></svg><b>Call us:</b>(555) 201 4870</div></div>
  <div class="abs contact-info" style="top:2458px"><div><svg class="ico" width="12" height="10" viewBox="0 0 12 10"><rect width="12" height="10" fill="#e3242b"/><path d="M0 0 L6 5 L12 0" stroke="#000" fill="none"/></svg><b>E-mail:</b>Hello@VelaModels.com</div></div>
  <div class="abs field" style="top:2316px">Full Name</div>
  <div class="abs field" style="top:2364px">Email</div>
  <div class="abs field" style="top:2413px">Phone</div>
  <div class="abs field" style="top:2461px">Address</div>
  <div class="abs message">Message</div>
  <div class="abs btn-red submit">Submit</div>
</section>

<footer class="abs footer">
  <p>Copyright © 2017 Vela Models. All Rights Reserved.</p>
  <div class="cards" aria-label="Accepted payment methods"><span></span><span></span><span></span><span></span><span></span></div>
</footer>

</body>
</html>
```